Container Web Design Project

I need the front page of my website to have a new, fresh look.
Our company is a highly specialized marketplace for shipping containers (yes, the 20' and 40' kind). Basically, think of Quibzo for shipping containers.
I have all of the links/content that I need plugged into a wireframe (attached), and the core color (blue #0073a2) of our existing site should stay the same as we've got stationary, business cards, marketing materials...
If you have any questions please ask.

```html
<!DOCTYPE html>
<html lang="en">
<head>
<meta charset="utf-8">
<title>BoxBidder.com – Shipping Container Marketplace</title>
<link href="https://fonts.googleapis.com/css2?family=Open+Sans:wght@400;600;700&family=Roboto+Condensed:wght@400;700&display=swap" rel="stylesheet">
<style>
:root{
  --blue:#0073a2;
  --blue-dark:#005b82;
  --blue-light:#1588b8;
  --page:#ebebeb;
  --white:#ffffff;
  --ink:#222222;
  --muted:#555555;
  --line:#d6d6d6;
  --green:#5aa51c;
  --green-dark:#3f8a0c;
  --cell:#f4f4f4;
}
*{box-sizing:border-box;margin:0;padding:0}
html,body{width:897px;height:1200px;overflow:hidden}
body{background:var(--page);font-family:"Open Sans",Arial,sans-serif;color:var(--ink);position:relative}
.abs{position:absolute}

/* header */
.header{left:104px;top:25px;width:689px;height:67px;background:var(--white);border-radius:4px 4px 0 0}
.brand{left:10px;top:13px;display:flex;align-items:center;gap:8px}
.brand-square{width:14px;height:14px;background:var(--blue)}
.brand-name{font-family:"Roboto Condensed",Arial,sans-serif;font-weight:700;font-size:30px;color:var(--blue);letter-spacing:-.3px}
.top-links{right:10px;top:8px;font-size:8.5px;color:var(--ink)}
.top-links span{margin:0 4px;color:#888}
.phone{right:6px;top:40px;font-size:18px;font-weight:700;color:var(--blue)}
.main-nav{left:104px;top:92px;width:689px;height:41px;background:var(--blue);display:flex;justify-content:space-around;align-items:center;border-radius:0 0 3px 3px}
.main-nav a{font-family:"Roboto Condensed",Arial,sans-serif;color:var(--white);font-size:11.5px;text-decoration:none;letter-spacing:-.2px}

/* search */
.search-field{left:121px;top:149px;width:372px;height:26px;background:var(--white);font-size:10px;color:#999;padding:8px 10px}
.search-field svg{position:absolute;right:8px;top:5px}
.select{top:149px;height:26px;background:var(--white);font-size:10px;padding:7px 8px;color:#333}
.select .chev{position:absolute;right:0;top:0;width:23px;height:26px;background:#111;display:flex;align-items:center;justify-content:center}
.search-btn{left:689px;top:149px;width:74px;height:26px;background:var(--blue);color:var(--white);font-weight:700;font-size:12.5px;display:flex;align-items:center;justify-content:center;border-radius:2px}

/* sidebar */
.side-nav{left:104px;top:193px;width:175px}
.side-nav a{display:block;height:25px;margin-bottom:2.6px;background:linear-gradient(var(--blue-light),var(--blue-dark));color:var(--white);font-family:"Roboto Condensed",Arial,sans-serif;font-size:11.3px;padding:5px 7px;text-decoration:none;border-radius:2px}
.newsletter{left:104px;top:420px;width:175px;height:81px;background:linear-gradient(var(--green),var(--green-dark));border-radius:2px}
.newsletter h3{font-family:"Roboto Condensed",Arial,sans-serif;font-weight:400;color:var(--white);font-size:12.5px;position:absolute;left:7px;top:9px}
.newsletter .input{position:absolute;left:8px;top:32px;width:160px;height:17px;background:var(--white);border-radius:2px}
.newsletter .submit{position:absolute;left:51px;top:56px;width:72px;height:18px;background:var(--blue);color:var(--white);font-size:12px;font-weight:700;text-align:center;line-height:18px;border-radius:2px}
.promo{left:104px;top:512px;width:175px;height:72px;background:linear-gradient(90deg,#f6f0e2,#e2d5b8 60%,#b89a6c);border-radius:2px;overflow:hidden}
.promo h3{position:absolute;left:8px;top:6px;font-family:"Roboto Condensed",Arial,sans-serif;font-size:18px;font-weight:700;color:#1a1a1a}
.promo p{position:absolute;left:8px;top:26px;font-family:"Roboto Condensed",Arial,sans-serif;font-size:12px;font-weight:700;color:#1a1a1a}
.promo .more{position:absolute;left:9px;top:47px;background:var(--blue);color:var(--white);font-size:9px;font-weight:700;padding:2px 8px;border-radius:2px}
.promo .art{position:absolute;right:12px;bottom:0;width:48px;height:32px;background:#c8282c}
.seller{left:104px;width:175px;height:71px;background:linear-gradient(#f3f3f3,#c9c9c9);border:1px solid #bdbdbd;border-radius:3px;text-align:center;font-family:"Roboto Condensed",Arial,sans-serif;color:#164a63;padding-top:12px}
.seller strong{display:block;font-size:19px;line-height:20px}
.seller span{font-size:12px;font-weight:700}

/* map + products */
.map{left:286px;top:193px;width:507px;height:232px;background:radial-gradient(circle at 60% 60%,#9ec8e8 0 6%,transparent 7%),linear-gradient(135deg,#ede6d6,#e6dfcd 40%,#d9e4c5 70%,#ede6d6)}
.products{left:286px;top:433px;width:507px;display:flex;justify-content:space-between}
.product{width:97px;font-size:9.5px;line-height:11px;color:var(--blue)}
.product .ph{height:88px;margin-bottom:4px;border:1px solid #e2e2e2;background:var(--white);display:flex;align-items:center;justify-content:center}
.product .ph div{width:62px;height:48px}
.product b{font-weight:700;display:block}

/* listings table */
.listings{left:286px;top:593px;width:507px;border-collapse:collapse;background:var(--white);font-size:8.8px;line-height:11px}
.listings th{height:31px;background:linear-gradient(var(--blue-light),var(--blue-dark));color:var(--white);font-weight:400;font-size:13.5px;text-align:left;padding-left:9px;border-left:1px solid #3a8fb6}
.listings td{height:88px;vertical-align:top;padding:13px 9px 0;border:1px solid var(--line)}
.listings td.shade{background:var(--cell)}
.thumb{width:75px;height:60px;border:3px solid var(--white);box-shadow:0 0 2px #999;margin-top:-1px}
.listings .ttl{color:var(--blue)}
.price{font-size:11px}

/* footer */
.legal{left:104px;top:993px;width:689px;height:64px;background:var(--blue);color:var(--white);font-size:9.8px;text-align:center;line-height:11px;padding:16px 30px}
.foot-col{top:1075px;font-size:10.3px;line-height:18px;color:#333}
.foot-brand{left:618px;top:1085px;font-family:"Roboto Condensed",Arial,sans-serif;font-weight:700;font-size:28px;color:#8a8a8a}
.rule{left:104px;top:1155px;width:689px;height:1px;background:#bbb}
.copy{left:0;top:1170px;width:897px;text-align:center;font-size:9.5px;color:#222}
</style>
</head>
<body>

<header class="abs header">
  <div class="abs brand"><div class="brand-square"></div><div class="brand-name">BoxBidder.com</div></div>
  <div class="abs top-links">Create and Account<span>|</span>Login<span>|</span>About BoxBidder.com<span>|</span>Contact Us</div>
  <div class="abs phone">(555) 014-2290</div>
</header>
<nav class="abs main-nav">
  <a href="#">20' SHIPPING CONTAINERS</a><a href="#">40' SHIPPING CONTAINERS</a><a href="#">40' HIGH CUBE CONTAINERS</a><a href="#">OPEN TOP CONTAINERS</a><a href="#">HOW TO BUY A SHIPPING CONTAINER</a>
</nav>

<div class="abs search-field">City, State or Country
  <svg width="16" height="16" viewBox="0 0 16 16"><circle cx="6.5" cy="6.5" r="5" fill="none" stroke="#777" stroke-width="2"/><line x1="10" y1="10" x2="15" y2="15" stroke="#777" stroke-width="2.2"/></svg>
</div>
<div class="abs select" style="left:505px;width:107px">Container Type<div class="chev"><svg width="12" height="8" viewBox="0 0 12 8"><polyline points="1,1 6,6 11,1" fill="none" stroke="#fff" stroke-width="2.4"/></svg></div></div>
<div class="abs select" style="left:617px;width:65px">Units<div class="chev"><svg width="12" height="8" viewBox="0 0 12 8"><polyline points="1,1 6,6 11,1" fill="none" stroke="#fff" stroke-width="2.4"/></svg></div></div>
<div class="abs search-btn">Search</div>

<aside class="abs side-nav">
  <a href="#">How to Buy Shipping Containers</a>
  <a href="#">New Listings</a>
  <a href="#">News and Articles</a>
  <a href="#">About BoxBidder.com</a>
  <a href="#">Container Weights and Dimensions</a>
  <a href="#">BoxBidder.com FAQs</a>
  <a href="#">Shipping Container Terms</a>
  <a href="#">How to Sell Your Containers</a>
</aside>
<div class="abs newsletter"><h3>Subscribe to Our Newsletter</h3><div class="input"></div><div class="submit">Submit</div></div>
<div class="abs promo"><h3>Phasellus ut</h3><p>libero ut nulla</p><div class="more">Read More</div><div class="art" role="img" aria-label="Red metal toolbox"></div></div>
<div class="abs seller" style="top:593px"><strong>Featured Seller</strong><span>logo will come here</span></div>
<div class="abs seller" style="top:674px"><strong>Featured Seller</strong><span>logo will come here</span></div>
<div class="abs seller" style="top:755px"><strong>Featured Seller</strong><span>logo will come here</span></div>

<div class="abs map" role="img" aria-label="Street map of central London with a location pin near the river"></div>

<section class="abs products">
  <div class="product"><div class="ph"><div role="img" aria-label="Open cardboard boxes" style="background:#c99a5e"></div></div><b>Nam quis ligula</b>Container Type<br>Location:<br>Price: $00.00</div>
  <div class="product"><div class="ph"><div role="img" aria-label="Stacked cardboard boxes" style="background:#b88a55;width:40px;height:70px"></div></div><b>Nam quis ligula</b>Container Type<br>Location:<br>Price: $00.00</div>
  <div class="product"><div class="ph"><div role="img" aria-label="Green shipping container on a crane hook" style="background:#4caf3c;width:85px;height:45px"></div></div><b>Nam quis ligula</b>Container Type<br>Location:<br>Price: $00.00</div>
  <div class="product"><div class="ph"><div role="img" aria-label="White tissue box" style="background:#e8e8e4;width:44px;height:58px"></div></div><b>Nam quis ligula</b>Container Type<br>Location:<br>Price: $00.00</div>
  <div class="product"><div class="ph"><div role="img" aria-label="Red shipping container" style="background:#d4332c;width:85px;height:48px"></div></div><b>Nam quis ligula</b>Container Type<br>Location:<br>Price: $00.00</div>
</section>

<table class="abs listings">
  <tr><th style="width:97px;border-left:0"></th><th style="width:151px">Listing Name</th><th style="width:101px">Container</th><th style="width:93px">Type</th><th>Price</th></tr>
  <tr><td><div class="thumb" role="img" aria-label="Forklift in a warehouse" style="background:linear-gradient(#b07a3a,#6d5a3c)"></div></td><td><span class="ttl">Nam quis ligula a nibh fermentum venenatis vitae</span> nec neque. Etiam non felis mi. Quisque feugiat, lectus non feugiat consectetur,</td><td class="shade"><span class="ttl">Nam quis ligula a</span> nec neque. Etiam non felis mi.</td><td class="shade"><span class="ttl">Nam quis ligula</span> nec neque. Etiam non felis mi.</td><td class="shade price">$ 00.00</td></tr>
  <tr><td><div class="thumb" role="img" aria-label="Pile of cardboard boxes" style="background:linear-gradient(#f1e6d6,#c49a68)"></div></td><td><span class="ttl">Nam quis ligula a nibh fermentum venenatis vitae</span> nec neque. Etiam non felis mi. Quisque feugiat, lectus non feugiat consectetur,</td><td class="shade"><span class="ttl">Nam quis ligula a</span> nec neque. Etiam non felis mi.</td><td class="shade"><span class="ttl">Nam quis ligula</span> nec neque. Etiam non felis mi.</td><td class="shade price">$ 00.00</td></tr>
  <tr><td><div class="thumb" role="img" aria-label="Wooden crate" style="background:linear-gradient(#8a6a4a,#5a4030)"></div></td><td><span class="ttl">Nam quis ligula a nibh fermentum venenatis vitae</span> nec neque. Etiam non felis mi. Quisque feugiat, lectus non feugiat consectetur,</td><td class="shade"><span class="ttl">Nam quis ligula a</span> nec neque. Etiam non felis mi.</td><td class="shade"><span class="ttl">Nam quis ligula</span> nec neque. Etiam non felis mi.</td><td class="shade price">$ 00.00</td></tr>
  <tr><td><div class="thumb" role="img" aria-label="Colourful boxes on a blue background" style="background:linear-gradient(#1a8fd0,#f2b21a 50%,#d8482a)"></div></td><td><span class="ttl">Nam quis ligula a nibh fermentum venenatis vitae</span> nec neque. Etiam non felis mi. Quisque feugiat, lectus non feugiat consectetur,</td><td class="shade"><span class="ttl">Nam quis ligula a</span> nec neque. Etiam non felis mi.</td><td class="shade"><span class="ttl">Nam quis ligula</span> nec neque. Etiam non felis mi.</td><td class="shade price">$ 00.00</td></tr>
</table>

<footer>
  <div class="abs legal">Copyright © 2011-2013 BoxBidder, Inc. All Rights Reserved. BoxBidder.com is a trademark of BoxBidder Inc. Designated trademarks and brands are the property of their respective owners. Use of this Web site constitutes acceptance of the BoxBidder user agrement and privacy policy.</div>
  <div class="abs foot-col" style="left:105px">Privacy Policy<br>User Agreement<br>Help</div>
  <div class="abs foot-col" style="left:213px">About BoxBidder.com<br>News and Articles<br>Contact Information</div>
  <div class="abs foot-col" style="left:374px">Glossary<br>Container Dimensions and Weights<br>Browse Locations</div>
  <div class="abs foot-brand">BoxBidder.com</div>
  <div class="abs rule"></div>
  <div class="abs copy">© Copyright 2013. All Rights Reserved.</div>
</footer>

</body>
</html>
```